The Harvest Compass

Cutting Through the Noise to What Actually Works.

Nutrition book

Target Market(s)

People looking to be or get healthy and eat right.

```html
<!DOCTYPE html>
<html lang="en">
<head>
<meta charset="UTF-8">
<title>The Harvest Compass – Promo</title>
<link href="https://fonts.googleapis.com/css2?family=Montserrat:wght@400;500;600;700;800&display=swap" rel="stylesheet">
<style>
  :root {
    --brand-green: #3f9a78;
    --brand-green-dark: #2f8a68;
    --mint: #a3e3c4;
    --mint-soft: #cdeedd;
    --canvas-light: #f1f1f0;
    --page-white: #ffffff;
    --ink: #1f2523;
    --ink-soft: #6d7471;
    --rule: #d9dedb;
    --panel-dark: #2a2e2d;
    --chalk: #2b2d2b;
    --chalk-frame: #6b4a2d;
    --chalk-text: #e9e7e0;
  }
  * { box-sizing: border-box; margin: 0; padding: 0; }
  html, body { width: 1200px; height: 1200px; overflow: hidden; }
  body {
    font-family: "Montserrat", sans-serif;
    background: var(--canvas-light);
    position: relative;
    color: var(--ink);
  }
  .hero-band {
    position: absolute; left: 0; top: 0; width: 1200px; height: 656px;
    background: var(--brand-green);
  }
  .hero-title {
    position: absolute; left: 0; top: 118px; width: 1200px;
    text-align: center; color: #fff;
    font-weight: 800; font-size: 138px; line-height: 1.05; letter-spacing: 1px;
  }

  /* Interior page thumbnails */
  .page {
    position: absolute; width: 216px;
    background: var(--page-white);
    box-shadow: 0 2px 6px rgba(0,0,0,0.12);
    overflow: hidden;
  }
  .page::before {
    content: ""; position: absolute; left: 0; top: 0; right: 0; height: 7px;
    background: var(--brand-green);
  }
  .page-label {
    position: absolute; left: 16px; top: 12px;
    font-size: 5.5px; font-weight: 600; letter-spacing: 0.6px; color: var(--ink-soft);
  }
  .page-mark {
    position: absolute; right: 8px; top: 10px; width: 32px; height: 32px;
    border-radius: 50%; background: var(--mint-soft);
  }
  .page-title {
    position: absolute; left: 16px; top: 26px; width: 160px;
    font-size: 13.5px; font-weight: 800; line-height: 1.1; color: var(--ink);
  }
  .page-sub {
    position: absolute; left: 16px; font-size: 6px; font-weight: 600; color: var(--ink-soft);
  }
  .page-foot {
    position: absolute; left: 0; right: 0; bottom: 0; height: 22px;
    border-top: 5px solid var(--brand-green);
    display: flex; gap: 4px; align-items: center; padding-left: 14px;
  }
  .page-foot span {
    width: 7px; height: 7px; border-radius: 50%; background: var(--brand-green);
  }
  .food-list { position: absolute; left: 16px; top: 78px; width: 185px; }
  .food-row { display: flex; align-items: center; gap: 7px; height: 26px; }
  .food-swatch { width: 20px; height: 16px; border-radius: 3px; flex: none; }
  .food-row p { font-size: 6.5px; font-weight: 600; color: var(--ink); flex: 1; }
  .food-row i {
    display: block; height: 2px; background: var(--rule); margin-top: 3px; width: 100%;
  }
  .bubble {
    position: absolute; width: 46px; height: 46px; border-radius: 50%;
    background: var(--mint-soft); display: flex; align-items: center; justify-content: center;
    font-size: 6px; font-weight: 700; color: var(--ink);
  }
  .text-bar { position: absolute; left: 16px; height: 2px; background: var(--rule); }
  .recipe-box {
    position: absolute; width: 84px; height: 84px; border: 1.5px solid var(--brand-green);
    border-radius: 6px; padding: 14px 8px 6px;
  }
  .recipe-box b {
    position: absolute; top: -6px; left: 10px; background: #fff; padding: 0 3px;
    font-size: 5.5px; font-weight: 800; color: var(--brand-green-dark);
  }
  .recipe-box i { display: block; height: 2px; background: var(--rule); margin-bottom: 7px; }
  .mini-list {
    position: absolute; font-size: 6px; font-weight: 600; color: var(--ink);
    line-height: 2.6;
  }
  .mini-list li { list-style: none; display: flex; align-items: center; gap: 5px; }
  .mini-list li::before {
    content: ""; width: 8px; height: 8px; border-radius: 2px; background: var(--mint);
  }

  /* Book cover */
  .book-cover {
    position: absolute; left: 627px; top: 428px; width: 514px; height: 732px;
    background: var(--panel-dark);
    box-shadow: 0 10px 28px rgba(0,0,0,0.3);
  }
  .cover-photo {
    position: absolute; left: 0; top: 0; width: 514px; height: 463px;
    background: radial-gradient(circle at 50% 45%, #7d807d 0%, #5c5f5c 55%, #494b49 100%);
  }
  .chalkboard {
    position: absolute; left: 135px; top: 182px; width: 246px; height: 152px;
    background: var(--chalk); border: 9px solid var(--chalk-frame);
    display: flex; flex-direction: column; align-items: center; justify-content: center;
    color: var(--chalk-text); text-align: center;
  }
  .chalkboard .chalk-title { font-size: 26px; font-weight: 500; line-height: 1.15; letter-spacing: 1px; }
  .chalkboard .chalk-sub {
    margin-top: 8px; padding-top: 6px; border-top: 1px solid rgba(233,231,224,0.5);
    font-size: 12px; font-weight: 500; letter-spacing: 1.5px;
  }
  .cover-panel {
    position: absolute; left: 0; top: 463px; width: 514px; height: 269px;
    border-top: 4px solid var(--mint);
  }
  .author-portrait {
    position: absolute; left: 197px; top: 402px; width: 122px; height: 122px;
    border-radius: 50%; border: 4px solid var(--mint);
    background: linear-gradient(160deg, #a8b3b6, #5d6a70);
  }
  .cover-tagline {
    position: absolute; right: 28px; top: 478px; width: 180px; text-align: center;
    font-size: 12px; font-weight: 700; line-height: 1.3; color: var(--mint);
  }
  .cover-author {
    position: absolute; left: 0; width: 514px; top: 543px; text-align: center;
    font-size: 15px; font-weight: 500; color: #fff;
  }
  .cover-headline {
    position: absolute; left: 0; width: 514px; top: 575px; text-align: center;
    font-size: 36px; font-weight: 800; line-height: 1.12; color: var(--mint); letter-spacing: 0.5px;
  }
  .cover-subline {
    position: absolute; left: 0; width: 514px; top: 672px; text-align: center;
    font-size: 13px; font-weight: 600; letter-spacing: 1px; color: #c9cfcc;
  }
</style>
</head>
<body>
  <div class="hero-band"></div>
  <h1 class="hero-title">THE HARVEST<br>COMPASS</h1>

  <!-- Row 1 -->
  <section class="page" style="left:26px; top:482px; height:282px;">
    <span class="page-label">HARVEST COMPASS</span><span class="page-mark"></span>
    <h2 class="page-title">AUTHOR'S PERFECT MEAL ANATOMY</h2>
    <div class="food-list">
      <div class="food-row"><span class="food-swatch" role="img" aria-label="Photo of lean protein" style="background:#b0563f"></span><p>Lean protein first<i></i></p></div>
      <div class="food-row"><span class="food-swatch" role="img" aria-label="Photo of greens" style="background:#7fae4e"></span><p>Crisp green leaves<i></i></p></div>
      <div class="food-row"><span class="food-swatch" role="img" aria-label="Photo of grains" style="background:#9b6b3e"></span><p>Whole grain base<i></i></p></div>
      <div class="food-row"><span class="food-swatch" role="img" aria-label="Photo of oil" style="background:#c6a347"></span><p>Healthy fat drizzle<i></i></p></div>
      <div class="food-row"><span class="food-swatch" role="img" aria-label="Photo of fruit" style="background:#3f7a3a"></span><p>Fresh fruit side<i></i></p></div>
      <div class="food-row"><span class="food-swatch" role="img" aria-label="Photo of nuts" style="background:#b58c5e"></span><p>Seeds and nuts<i></i></p></div>
    </div>
    <div class="page-foot"><span></span><span></span><span></span></div>
  </section>

  <section class="page" style="left:258px; top:482px; height:282px;">
    <span class="page-label">HARVEST COMPASS</span><span class="page-mark"></span>
    <h2 class="page-title">SIGNATURE VITAMIN INSIGHTS</h2>
    <span class="page-sub" style="top:62px;">Key daily nutrients</span>
    <svg style="position:absolute; left:58px; top:118px;" width="100" height="100" viewBox="0 0 100 100" role="img" aria-label="Pie chart of a balanced plate">
      <circle cx="50" cy="50" r="48" fill="#ffffff" stroke="#d9dedb" stroke-width="2"/>
      <path d="M50 50 L50 4 A46 46 0 0 1 96 50 Z" fill="#c98a4a"/>
      <path d="M50 50 L96 50 A46 46 0 0 1 50 96 Z" fill="#b9503f"/>
      <path d="M50 50 L50 96 A46 46 0 0 1 4 50 Z" fill="#6fa84a"/>
      <path d="M50 50 L4 50 A46 46 0 0 1 50 4 Z" fill="#e0b552"/>
    </svg>
    <div class="bubble" style="left:16px; top:76px;">FATS</div>
    <div class="bubble" style="left:156px; top:76px;">CARBS</div>
    <div class="bubble" style="left:16px; top:196px;">VEGGIES</div>
    <div class="bubble" style="left:156px; top:196px;">PROTEIN</div>
    <div class="page-foot"><span></span><span></span><span></span></div>
  </section>

  <section class="page" style="left:492px; top:482px; height:282px;">
    <span class="page-label">HARVEST COMPASS</span><span class="page-mark"></span>
    <h2 class="page-title">PLANT-BASED NUTRITIONAL COMPARISON</h2>
    <span style="position:absolute; left:6px; top:250px; transform:rotate(-90deg); transform-origin:left top; font-size:9px; font-weight:800; color:var(--brand-green); white-space:nowrap;">PROTEIN PER 240ML SERVING</span>
    <div role="img" aria-label="Photos of plant milk bottles" style="position:absolute; left:48px; top:88px; width:120px; height:64px; background:linear-gradient(#eef0ef,#dfe3e1);"></div>
    <span class="page-sub" style="top:158px; left:52px;">OAT</span>
    <span class="page-sub" style="top:158px; left:94px;">SOY</span>
    <span class="page-sub" style="top:158px; left:134px;">PEA</span>
    <div role="img" aria-label="Photos of plant milk bottles" style="position:absolute; left:48px; top:176px; width:120px; height:64px; background:linear-gradient(#eef0ef,#dfe3e1);"></div>
    <div class="page-foot"><span></span><span></span><span></span></div>
  </section>

  <!-- Row 2 -->
  <section class="page" style="left:26px; top:808px; height:305px;">
    <span class="page-label">HARVEST COMPASS</span><span class="page-mark"></span>
    <h2 class="page-title">AUTHOR'S PERFECT ANATOMY</h2>
    <div role="img" aria-label="Illustration of a balanced plate held by hands" style="position:absolute; left:96px; top:66px; width:96px; height:80px; border-radius:50%; background:radial-gradient(circle,#f3e4cf,#c8d9b8);"></div>
    <span class="page-sub" style="top:96px;">Plate basics</span>
    <ul class="mini-list" style="left:16px; top:160px;"><li>Protein</li><li>Grains</li><li>Greens</li></ul>
    <ul class="mini-list" style="left:110px; top:160px;"><li>Fruit</li><li>Dairy</li><li>Oils</li></ul>
    <div class="page-foot"><span></span><span></span><span></span></div>
  </section>

  <section class="page" style="left:258px; top:808px; height:305px;">
    <span class="page-label">HARVEST COMPASS</span><span class="page-mark"></span>
    <h2 class="page-title">AUTHOR'S BALANCED RECIPES</h2>
    <span class="page-sub" style="top:66px;">Why these recipes</span>
    <p style="position:absolute; left:16px; top:80px; width:180px; font-size:6px; color:var(--ink-soft); line-height:1.5;">Simple meals built on whole foods you enjoy.</p>
    <span class="text-bar" style="top:104px; width:176px;"></span>
    <span class="text-bar" style="top:112px; width:150px;"></span>
    <span class="text-bar" style="top:120px; width:168px;"></span>
    <div class="recipe-box" style="left:16px; top:168px;"><b>BREAKFAST</b><i></i><i></i><i></i><i></i><i></i><i></i></div>
    <div class="recipe-box" style="left:114px; top:168px;"><b>DINNER</b><i></i><i></i><i></i><i></i><i></i><i></i></div>
    <div class="page-foot"><span></span><span></span><span></span></div>
  </section>

  <section class="page" style="left:492px; top:808px; height:305px;">
    <span class="page-label">HARVEST COMPASS</span><span class="page-mark"></span>
    <h2 class="page-title">WELLNESS RITUALS</h2>
    <span class="page-sub" style="top:48px;">Daily habit split</span>
    <svg style="position:absolute; left:22px; top:74px;" width="100" height="100" viewBox="0 0 100 100" role="img" aria-label="Pie chart of daily habits">
      <path d="M50 50 L50 4 A46 46 0 0 1 96 50 Z" fill="#6fa84a"/>
      <path d="M50 50 L96 50 A46 46 0 0 1 30 92 Z" fill="#c94b44"/>
      <path d="M50 50 L30 92 A46 46 0 0 1 50 4 Z" fill="#3f9a78"/>
    </svg>
    <div class="page-foot"><span></span><span></span><span></span></div>
  </section>

  <!-- Row 3 -->
  <section class="page" style="left:26px; top:1131px; height:120px;">
    <span class="page-label">HARVEST COMPASS</span><span class="page-mark"></span>
    <h2 class="page-title">WELLNESS RITUALS</h2>
  </section>
  <section class="page" style="left:258px; top:1131px; height:120px;">
    <span class="page-label">HARVEST COMPASS</span><span class="page-mark"></span>
    <h2 class="page-title">AUTHOR'S WELLNESS PHILOSOPHY</h2>
  </section>
  <section class="page" style="left:492px; top:1131px; height:120px;">
    <span class="page-label">HARVEST COMPASS</span><span class="page-mark"></span>
    <h2 class="page-title">AUTHOR'S WELLNESS PHILOSOPHY</h2>
  </section>

  <!-- Book cover -->
  <article class="book-cover">
    <div class="cover-photo" role="img" aria-label="Overhead photo of whole foods: almonds, bread, peas, salmon, tomatoes, steak, star fruit, nuts and a leather notebook on slate"></div>
    <div class="chalkboard">
      <span class="chalk-title">THE HARVEST<br>COMPASS</span>
      <span class="chalk-sub">AUTHOR'S BLUEPRINT</span>
    </div>
    <div class="cover-panel"></div>
    <div class="author-portrait" role="img" aria-label="Portrait photo of the author"></div>
    <p class="cover-tagline">EXPLORE THE HIERARCHY<br>&amp; YOUR BLUEPRINT</p>
    <p class="cover-author">Dr. Mara Ellison, Ph.D. – Author &amp; Health Coach</p>
    <h2 class="cover-headline">THE BLUEPRINT FOR<br>HEALTH &amp; FITNESS</h2>
    <p class="cover-subline">EXPLORE THE HIERARCHY &amp; YOUR BLUEPRINT</p>
  </article>
</body>
</html>
```